Survey App for phone users trying a new phone with Dual connectivity

Survey App Brief<br/>Design For an Android Survey App for users' feedback on Call, SMS, Data and Streaming Experience on their Mobile phones.<br/><br/>Purpose of the App<br/>To ensure that the user's experience is not impacted by the network switching between two network on the special mobile phones they newly started using.<br/><br/>App Requirements:<br/>First screen: The registration screen, where the user needs to enter the following:<br/>Name: text box<br/>Phone Number: text box<br/>Group Number : <br/><br/>An information text:<br/>By Registering I agree to participate in the Survey.<br/><br/>Register: Button<br/><br/>Start Screen - Survey screens (next time user open the App this will be the first screen):<br/>We need feedback for 4 indicators:<br/>Call Experience<br/>SMS Experience<br/>Data Experience<br/>Streaming Experience<br/><br/>Each Experience can be in the form of a questionnaire or Satisfied/ Somewhat Satisfied / Extremely Satisfied form with radio buttons or on a scale of 1 to 5. We need to ensure that the format used is very professional.<br/><br/>An optional text box for the user to enter the comment in a free format.<br/><br/>This can be done in 4 different screens or in one single screen if it does not give a clumsy look.<br/><br/>A Send button at the end to submit the Survey.<br/><br/>We need a burger menu at the top left corner of this screen, which when expanded will provide 5 options:<br/>Edit User Profile<br/>Survey interval Timer<br/>FAQ<br/>Exit<br/>About<br/><br/><br/>Please ensure that the app is simple, friendly, lively and professional at the same time so that it ignites an interest in the user to use the app.<br/>Use Logo as appropriate.
Telecommunications
Colors
Designer to choose colors to be used in the design.

```html
<!DOCTYPE html>
<html lang="en">
<head>
<meta charset="utf-8">
<title>Survey App – Screens</title>
<link rel="stylesheet" href="https://fonts.googleapis.com/css2?family=Lato:wght@400;700;900&display=swap">
<style>
  :root {
    --stage-bg: #2e4a9e;
    --brand: #2ca9e1;
    --brand-light: #5cc3ef;
    --menu-bg: #3bb5e3;
    --ink: #222;
    --ink-soft: #555;
    --line: #d6d6d6;
    --white: #fff;
  }
  * { box-sizing: border-box; margin: 0; padding: 0; }
  html, body { width: 1200px; height: 691px; overflow: hidden; background: var(--stage-bg); }
  body { font-family: "Lato", sans-serif; color: var(--ink); }

  .stage {
    position: relative; width: 1588px; height: 915px;
    transform: scale(0.7557); transform-origin: 0 0;
  }
  .screen { position: absolute; top: 52px; width: 450px; background: var(--white); overflow: hidden; }
  .screen--register { left: 75px; height: 717px; }
  .screen--survey { left: 551px; height: 810px; }
  .screen--menu { left: 1063px; height: 810px; }

  .screen__backdrop {
    position: absolute; left: 0; top: 0; width: 450px; height: 452px;
    background: linear-gradient(160deg, #2a86d4 0%, #4fb6ec 45%, #2f9be0 75%, #6cc9f2 100%);
  }

  .app-header {
    position: absolute; left: 16px; width: 418px; height: 92px;
    background: var(--white); border-radius: 14px;
  }
  .screen--register .app-header { top: 18px; }
  .screen--survey .app-header, .screen--menu .app-header { top: 12px; height: 91px; }
  .brand { position: absolute; left: 14px; top: 50%; transform: translateY(-50%); display: flex; align-items: center; gap: 8px; }
  .brand__mark { width: 40px; height: 40px; border-radius: 50%; background: var(--brand-light); }
  .brand__name { font-size: 12.5px; font-weight: 700; letter-spacing: 1.2px; line-height: 13px; color: #6b6b6b; }
  .burger { position: absolute; right: 15px; top: 50%; transform: translateY(-50%); width: 24px; height: 20px; }

  .card {
    position: absolute; left: 16px; width: 418px; bottom: 0;
    background: var(--white); border-radius: 14px 14px 0 0;
  }
  .screen--register .card { top: 125px; }
  .screen--survey .card, .screen--menu .card { top: 119px; }
  .card__title {
    position: absolute; left: 0; width: 100%; text-align: center;
    font-size: 27px; font-weight: 900; letter-spacing: 0.5px; top: 22px;
  }
  .screen--survey .card__title, .screen--menu .card__title { top: 22px; }
  .card__rule { position: absolute; left: 13px; width: 393px; top: 70px; border-top: 1px solid #bbb; }

  .field {
    position: absolute; left: 24px; width: 371px; height: 50px;
    border: 2px solid var(--line); border-radius: 25px;
    font-size: 14px; color: var(--ink-soft); padding: 15px 0 0 24px;
  }
  .field--area { height: 136px; border-radius: 14px; padding-top: 20px; }
  .consent { position: absolute; left: 25px; top: 455px; display: flex; align-items: center; gap: 15px; font-size: 14px; color: var(--ink-soft); }
  .consent__box { width: 22px; height: 22px; border: 2px solid var(--line); border-radius: 3px; }

  .btn {
    position: absolute; left: 23px; width: 373px; height: 52px; border-radius: 26px;
    background: var(--brand); color: var(--white); font-size: 23px; font-weight: 900;
    text-align: center; line-height: 52px; letter-spacing: 0.5px;
  }
  .repeat-note { position: absolute; right: 17px; font-size: 13px; }

  .question { position: absolute; left: 23px; font-size: 15.5px; font-weight: 900; }
  .scale { position: absolute; left: 24px; display: flex; gap: 12px; }
  .scale__option {
    width: 64px; height: 38px; border: 2px solid var(--line);
    display: flex; align-items: center; justify-content: center; font-size: 14px; font-weight: 700;
  }
  .comment {
    position: absolute; left: 23px; top: 462px; width: 368px; height: 127px;
    border: 2px solid var(--line); padding: 18px 16px; font-size: 15.5px; color: #444;
  }

  .side-menu {
    position: absolute; left: 246px; top: 49px; width: 175px; height: 214px;
    background: var(--menu-bg); color: var(--white);
  }
  .side-menu__close { position: absolute; right: 6px; top: 2px; font-size: 20px; font-weight: 900; }
  .side-menu__list { list-style: none; position: absolute; left: 17px; top: 33px; }
  .side-menu__item { font-size: 15.5px; height: 27px; line-height: 24px; display: flex; align-items: center; gap: 10px; }
  .side-menu__item::before { content: "›"; font-size: 16px; }
</style>
</head>
<body>
<div class="stage">

  <!-- Registration screen -->
  <section class="screen screen--register">
    <div class="screen__backdrop" role="img" aria-label="Blue abstract network photograph"></div>
    <header class="app-header">
      <div class="brand"><span class="brand__mark"></span><span class="brand__name">NORTHWIND<br>TELECOM</span></div>
      <svg class="burger" viewBox="0 0 24 20"><rect y="0" width="24" height="3.5" fill="#2ca9e1"/><rect y="8" width="24" height="3.5" fill="#2ca9e1"/><rect y="16" width="24" height="3.5" fill="#2ca9e1"/></svg>
    </header>
    <div class="card">
      <h1 class="card__title">REGISTRATION</h1>
      <div class="card__rule"></div>
      <div class="field" style="top:95px">NAME</div>
      <div class="field" style="top:163px">PHONE NUMBER</div>
      <div class="field" style="top:230px">GROUP NUMBER</div>
      <div class="field field--area" style="top:297px">AN INFORMATION TEXT</div>
      <div class="consent"><span class="consent__box"></span>By Registering I agree to participate in the Survey</div>
      <div class="btn" style="top:499px;left:22px">REGISTER</div>
      <div class="repeat-note" style="top:556px">X10</div>
    </div>
  </section>

  <!-- Survey screen -->
  <section class="screen screen--survey">
    <div class="screen__backdrop" role="img" aria-label="Blue abstract network photograph"></div>
    <header class="app-header">
      <div class="brand"><span class="brand__mark"></span><span class="brand__name">NORTHWIND<br>TELECOM</span></div>
      <svg class="burger" viewBox="0 0 24 20"><rect y="0" width="24" height="3.5" fill="#2ca9e1"/><rect y="8" width="24" height="3.5" fill="#2ca9e1"/><rect y="16" width="24" height="3.5" fill="#2ca9e1"/></svg>
    </header>
    <div class="card">
      <h1 class="card__title">START SURVEY</h1>
      <div class="card__rule"></div>
      <div class="question" style="top:98px">CALL EXPERIENCE</div>
      <div class="scale" style="top:130px"><span class="scale__option">1</span><span class="scale__option">2</span><span class="scale__option">3</span><span class="scale__option">4</span><span class="scale__option">5</span></div>
      <div class="question" style="top:188px">SMS EXPERIENCE</div>
      <div class="scale" style="top:220px"><span class="scale__option">1</span><span class="scale__option">2</span><span class="scale__option">3</span><span class="scale__option">4</span><span class="scale__option">5</span></div>
      <div class="question" style="top:278px">DATA EXPERIENCE</div>
      <div class="scale" style="top:310px"><span class="scale__option">1</span><span class="scale__option">2</span><span class="scale__option">3</span><span class="scale__option">4</span><span class="scale__option">5</span></div>
      <div class="question" style="top:368px">STREAMING EXPERIENCE</div>
      <div class="scale" style="top:400px"><span class="scale__option">1</span><span class="scale__option">2</span><span class="scale__option">3</span><span class="scale__option">4</span><span class="scale__option">5</span></div>
      <div class="comment">Enter your comment</div>
      <div class="btn" style="top:605px">SEND</div>
      <div class="repeat-note" style="top:655px">X10</div>
    </div>
  </section>

  <!-- Survey screen with menu open -->
  <section class="screen screen--menu">
    <div class="screen__backdrop" role="img" aria-label="Blue abstract network photograph"></div>
    <header class="app-header">
      <div class="brand"><span class="brand__mark"></span><span class="brand__name">NORTHWIND<br>TELECOM</span></div>
    </header>
    <div class="card">
      <h1 class="card__title">START SURVEY</h1>
      <div class="card__rule"></div>
      <div class="question" style="top:98px">CALL EXPERIENCE</div>
      <div class="scale" style="top:130px"><span class="scale__option">1</span><span class="scale__option">2</span><span class="scale__option">3</span><span class="scale__option">4</span><span class="scale__option">5</span></div>
      <div class="question" style="top:188px">SMS EXPERIENCE</div>
      <div class="scale" style="top:220px"><span class="scale__option">1</span><span class="scale__option">2</span><span class="scale__option">3</span><span class="scale__option">4</span><span class="scale__option">5</span></div>
      <div class="question" style="top:278px">DATA EXPERIENCE</div>
      <div class="scale" style="top:310px"><span class="scale__option">1</span><span class="scale__option">2</span><span class="scale__option">3</span><span class="scale__option">4</span><span class="scale__option">5</span></div>
      <div class="question" style="top:368px">STREAMING EXPERIENCE</div>
      <div class="scale" style="top:400px"><span class="scale__option">1</span><span class="scale__option">2</span><span class="scale__option">3</span><span class="scale__option">4</span><span class="scale__option">5</span></div>
      <div class="comment">Enter your comment</div>
      <div class="btn" style="top:605px">SEND</div>
      <div class="repeat-note" style="top:655px">X10</div>
    </div>
    <nav class="side-menu">
      <span class="side-menu__close">X</span>
      <ul class="side-menu__list">
        <li class="side-menu__item">Edit User Profile</li>
        <li class="side-menu__item">Survey interval</li>
        <li class="side-menu__item">Timer</li>
        <li class="side-menu__item">FAQ</li>
        <li class="side-menu__item">Exit</li>
        <li class="side-menu__item">About</li>
      </ul>
    </nav>
  </section>

</div>
</body>
</html>
```